CD cover Digipack For Singer & Songwriter

I need a Full Digipack CD cover without booklet, for my first album.

My Name is Marek Dolun and Im a Pastor and a singer & songwriter based in berlin.
All of the music is Christian/Gospel music, and has a soul flare to it. It is a unplugged/acoustic album.

It will be available to download from the label web shop as well as a limited physical release.

The title of the album is "Brighter Skies" and should be included on the cover and CD image.

The following information must be included in the Digipack.

Here are the tracks, this is the final order.

Tracks:

1 Cold Rain
2 Under Lanterns
3 Lights Along the River (Feat. Valumba)
4 Brighter Skies (Feat. Dax Frennick)
5 Open the Gate
6 Winter Carries Home
7 Slow Tide
8 Morgenrot
9 Stets Wach

On the inside of the Digipack I would like to have a short Bio (attached in the documents) you can format the content how you like.

I also need to include this information somewhere, I'll leave it up to you where to put it:

Recorded at Wespen Records in Berlin

Copyright ©2017 Wespen Records
www.wespen-records.com

Marek Dolun
www.marekdolun-music.com

Please also include all the documents attached to the Digipack:
Label name, label code etc...

Look And Feel: Elegant, Modern...

Target Market(s)

Christian Gospel / Unplugged Acoustic

Industry/Entity Type

Singer

Font styles to use
Serif
Sans Serif
Decorative
Script

Colors
ffffff

Requirements
Must have
• 1 Cold Rain (03:25)
• 2 Under Lanterns (02:44)
• 3 Lights Along the River (Feat. Valumba) (03:23)
• 4 Brighter Skies (Feat. Dax Frennick) (03.01)
• 5 Open the Gate (03:27)
• 6 Winter Carries Home (03:00)
• 7 Slow Tide (03:35)
• 8 Morgenrot (03:40)
• 9 Stets Wach (04:11)
• CD-Duration 29:06 minutes
• KT 40782
• On the inside of the Digipack I would like to have a short Bio (attached in the documents) you can format the content how you like.
• I also need to include this information somewhere, I'll leave it up to you where to put it:
• Recorded at Wespen Records in Berlin
• Copyright ©2017 Wespen Records
• www.wespenrecords.com
• Marek Dolun
• www.marekdolun-music.com
• Please also include all the documents attached to the Digipack:
• Label name, label code etc...

```html
<!DOCTYPE html>
<html lang="en">
<head>
<meta charset="utf-8">
<title>Brighter Skies – Back Cover</title>
<link rel="stylesheet" href="https://fonts.googleapis.com/css2?family=Rochester&family=Cormorant+Garamond:wght@500&display=swap">
<style>
  :root {
    --paper: #f5f5f5;
    --paper-mid: #e4e4e4;
    --suit: rgba(120,120,120,0.55);
    --suit-soft: rgba(160,160,160,0.25);
    --trouser: rgba(40,40,40,0.55);
    --ink: #161616;
    --ink-soft: #3c3c3c;
  }
  html, body {
    margin: 0;
    padding: 0;
    width: 1200px;
    height: 1200px;
    overflow: hidden;
    background: var(--paper);
  }
  .back-cover {
    position: relative;
    width: 1200px;
    height: 1200px;
    overflow: hidden;
    background: radial-gradient(ellipse at 90% 22%, #ffffff 0%, var(--paper) 35%, var(--paper-mid) 100%);
  }
  .artist-portrait {
    position: absolute;
    inset: 0;
    background:
      radial-gradient(ellipse 150px 260px at 880px 900px, var(--trouser) 0%, rgba(40,40,40,0) 100%),
      radial-gradient(ellipse 210px 330px at 920px 640px, var(--suit) 0%, rgba(120,120,120,0) 100%),
      radial-gradient(ellipse 330px 520px at 900px 720px, var(--suit-soft) 0%, rgba(160,160,160,0) 100%);
  }
  .tracklist {
    position: absolute;
    left: 56px;
    top: 222px;
    margin: 0;
    padding: 0;
    list-style: none;
    font-family: "Rochester", cursive;
    font-size: 46px;
    line-height: 80px;
    color: var(--ink);
    white-space: nowrap;
  }
  .track { margin: 0; }
  .track-time {
    font-family: "Cormorant Garamond", serif;
    font-size: 20px;
    color: var(--ink-soft);
    margin-left: 10px;
    letter-spacing: 0.5px;
  }
  .credits {
    position: absolute;
    left: 58px;
    top: 1000px;
    width: 440px;
    color: var(--ink);
  }
  .album-title {
    margin: 0 0 10px;
    font-family: "Rochester", cursive;
    font-size: 40px;
    font-weight: 400;
    line-height: 1;
  }
  .credit-line {
    margin: 0;
    font-family: "Cormorant Garamond", serif;
    font-size: 17px;
    line-height: 24px;
    color: var(--ink-soft);
    white-space: nowrap;
  }
</style>
</head>
<body>
  <main class="back-cover">
    <div class="artist-portrait" role="img" aria-label="Black and white photograph of the singer in a grey suit and tie, seated on a white ledge, looking down"></div>
    <ol class="tracklist">
      <li class="track">1. Cold Rain<span class="track-time">03:25</span></li>
      <li class="track">2. Under Lanterns<span class="track-time">02:44</span></li>
      <li class="track">3 .Lights Along the River (Feat. Valumba)<span class="track-time">03:23</span></li>
      <li class="track">4 .Brighter Skies (Feat. Dax Frennick)<span class="track-time">03:01</span></li>
      <li class="track">5. Open the Gate<span class="track-time">03:27</span></li>
      <li class="track">6. Winter Carries Home<span class="track-time">03:00</span></li>
      <li class="track">7 .Slow Tide<span class="track-time">03:35</span></li>
      <li class="track">8 .Morgenrot<span class="track-time">03:40</span></li>
      <li class="track">9. Stets Wach<span class="track-time">04:11</span></li>
    </ol>
    <section class="credits">
      <h1 class="album-title">Marek Dolun – Brighter Skies</h1>
      <p class="credit-line">CD-Duration 29:06 minutes · KT 40782</p>
      <p class="credit-line">Recorded at Wespen Records in Berlin</p>
      <p class="credit-line">Copyright ©2017 Wespen Records · www.wespenrecords.com</p>
      <p class="credit-line">Marek Dolun · www.marekdolun-music.com</p>
    </section>
  </main>
</body>
</html>
```